Coffee Shop needs a fresh new menu

Hi,
I would like a new menu to be designed for our coffee shop.
We display our menu on a television screen, so would need it in a file that would allow us to continue to do so -- I have attached a photo so that you can see our current design, and how it is displayed.

I'd like something that is easy to read, if the design could have a "hipster" feel to it -- we are located at a hospital and University.

I have attached a Word file with what we would like on the menu.

Feel free to contact me if you have any questions.

Thanks,
Tam

Just A4 size will be fine, and no need to include menu 1 and menu 2 - I just put them in as an example of what we already have -- they are our printed menu's. Thanks

Hospital

```html
<!DOCTYPE html>
<html lang="en">
<head>
<meta charset="utf-8">
<title>Coffee Shop Menu</title>
<link href="https://fonts.googleapis.com/css2?family=Crimson+Text:wght@400;600&display=swap" rel="stylesheet">
<style>
  :root {
    --coffee-bg: #f07479;
    --light-bg: #f7a3a6;
    --hot-bg: #ec1c24;
    --breakfast-bg: #ef4a51;
    --extras-bg: #141414;
    --text: #ffffff;
    --cup-tone: #e4636a;
    --cake-tone: #d99597;
    --sandwich-tone: #c7181f;
    --breakfast-tone: #f2713f;
  }
  * { margin: 0; padding: 0; box-sizing: border-box; }
  html, body { width: 1200px; height: 848px; overflow: hidden; background: #fff; }
  body { font-family: "Crimson Text", Georgia, serif; color: var(--text); }
  .menu { position: relative; width: 1200px; height: 848px; overflow: hidden; }
  .panel { position: absolute; }
  .panel--coffee { left: 0; top: 0; width: 603px; height: 409px; background: var(--coffee-bg); }
  .panel--light { left: 603px; top: 0; width: 597px; height: 409px; background: var(--light-bg); }
  .panel--hot { left: 0; top: 409px; width: 603px; height: 369px; background: var(--hot-bg); }
  .panel--breakfast { left: 603px; top: 409px; width: 597px; height: 369px; background: var(--breakfast-bg); }
  .extras { position: absolute; left: 0; top: 778px; width: 1200px; height: 70px; background: var(--extras-bg); text-align: center; }
  .extras__title { font-size: 21px; padding-top: 10px; line-height: 24px; }
  .extras__note { font-size: 15.5px; line-height: 20px; }

  .art { position: absolute; }
  .art--cup { left: 22px; top: 215px; width: 140px; height: 194px; background: var(--cup-tone); border-radius: 40px 40px 30px 30px; opacity: .6; }
  .art--cakes { left: 610px; top: 285px; width: 272px; height: 122px; background: radial-gradient(ellipse at 50% 55%, #e9b3b4 0%, var(--cake-tone) 60%, #a98a80 100%); border-radius: 50% 50% 45% 45%; opacity: .85; }
  .art--sandwich { left: 12px; top: 598px; width: 162px; height: 142px; background: var(--sandwich-tone); border-radius: 10px; }
  .art--breakfast { left: 625px; top: 628px; width: 250px; height: 138px; background: radial-gradient(ellipse, #f48a4a 0%, var(--breakfast-tone) 70%); border-radius: 50%; opacity: .9; }

  .heading { position: absolute; font-size: 21px; font-weight: 400; letter-spacing: .3px; line-height: 26px; }
  .list { position: absolute; list-style: none; font-size: 16.5px; line-height: 22.3px; }
  .price-row { display: grid; grid-template-columns: 138px 107px auto; }
</style>
</head>
<body>
<main class="menu">
  <section class="panel panel--coffee"></section>
  <section class="panel panel--light"></section>
  <section class="panel panel--hot"></section>
  <section class="panel panel--breakfast"></section>

  <div class="art art--cup" role="img" aria-label="Faint illustration of a coffee cup with a splash"></div>
  <div class="art art--cakes" role="img" aria-label="Illustration of cupcakes on a plate"></div>
  <div class="art art--sandwich" role="img" aria-label="Illustration of a sandwich"></div>
  <div class="art art--breakfast" role="img" aria-label="Illustration of toast, bacon and eggs on a plate"></div>

  <h2 class="heading" style="left:188px; top:30px;">COFFEE:</h2>
  <ul class="list" style="left:188px; top:77px;">
    <li class="price-row"><span>Latte</span><span>small $4.0</span><span>Large $4.50</span></li>
    <li class="price-row"><span>Cappuccino</span><span>small $4.0</span><span>Large $4.50</span></li>
    <li class="price-row"><span>Flat White</span><span>small $4.0</span><span>Large $4.50</span></li>
    <li class="price-row"><span>Long Black</span><span>small $4.0</span><span>Large $4.50</span></li>
    <li class="price-row"><span>Hot Chocolate</span><span>small $4.0</span><span>Large $4.50</span></li>
  </ul>
  <ul class="list" style="left:188px; top:210px;">
    <li class="price-row"><span>Chai Latte</span><span>small $4.50</span><span>Large $5.0</span></li>
    <li class="price-row"><span>Mocha</span><span>small $4.50</span><span>Large $5.0</span></li>
    <li class="price-row"><span>Dirty Chai</span><span>small $5</span><span>Large $5.50</span></li>
  </ul>
  <ul class="list" style="left:188px; top:299px;">
    <li>Espresso $3.50</li>
    <li>Short Macchiato $4.0</li>
    <li>Piccolo $4.0</li>
    <li>Long Macchiato $4.50</li>
  </ul>

  <h2 class="heading" style="left:801px; top:52px;">SOMETHING LIGHT:</h2>
  <ul class="list" style="left:801px; top:108px;">
    <li>Mixed Yoghurts $5.50</li>
    <li>Chia Pudding $5.50</li>
    <li>Fruit Salad $5.50</li>
    <li>Bircher Muesli $5.50</li>
    <li>Protein Balls $4.0</li>
    <li>Banana Bread $4.50</li>
    <li>Muffins $4.50</li>
    <li>Slices $4.0</li>
  </ul>

  <h2 class="heading" style="left:180px; top:437px;">HOT FOOD AND SANDWICHES:</h2>
  <ul class="list" style="left:180px; top:495px;">
    <li>Pre Made Sandwiches $6.50 - $7.50</li>
    <li>Pre Made Focaccias $8.50</li>
    <li>Wraps $7.50</li>
    <li>Vegetarian Salad $7.50</li>
    <li>Meat/Seafood Salad $9.50</li>
    <li>Hot Chips $4.50</li>
    <li>Dim Sim $1.50</li>
    <li>Potato Cake $1.50</li>
    <li>Plain Hamburger $7.50</li>
    <li>Hamburger with the lot $9.0</li>
    <li>Chicken Schnitzel Burger $8.50</li>
  </ul>

  <h2 class="heading" style="left:802px; top:444px;">BREAKFAST ITEMS:</h2>
  <ul class="list" style="left:802px; top:502px;">
    <li>Bacon, Egg and Cheese Roll $6.0</li>
    <li>Ham and Cheese Toastie $5.0</li>
    <li>Cheese and Tomato Toastie $5.0</li>
    <li>Ham and Cheese Croissant $6.0</li>
    <li>Cheese and Tomato Croissant $5.50</li>
    <li>Plain Croissant $3.50</li>
    <li>Hash Brown $2.0</li>
    <li>2 Piece Toast $3.0</li>
    <li>2 Piece Rasin Toast $3.0</li>
  </ul>

  <footer class="extras">
    <p class="extras__title">Extras</p>
    <p class="extras__note">Soy Milk/Lactose Free Milk/Syrups/Extra Shot/Decaf&nbsp; $0.50 extra</p>
  </footer>
</main>
</body>
</html>
```